Design a New Business Card for Our Company

We are looking for fresh, unique, and a modern business card that reflects our roots as digital marketing agency focused on SEM.

Industry/Entity Type

Marketing

Contact Information for Business Card

looking for very unique out of the box designs. clean and modern that compliments our logo

Requirements
Must have
• colors should match our logo
• Front should have name, address, email, and phone/fax of the person, phone/fax are the same number
• back should have our url

```html
<!DOCTYPE html>
<html lang="en">
<head>
<meta charset="utf-8">
<title>Brightpath Media – Business Card</title>
<link rel="stylesheet" href="https://fonts.googleapis.com/css2?family=Arimo:wght@400;700&display=swap">
<style>
  :root {
    --bg: #eceaeb;
    --card-light: #ffffff;
    --card-dark: #2e3033;
    --card-dark-glow: #45474b;
    --brand-blue: #4a8fd6;
    --brand-grey: #a9a9a9;
    --ink-light: #ffffff;
    --rule: #8a8c90;
  }
  * { box-sizing: border-box; margin: 0; padding: 0; }
  html, body { width: 1200px; height: 1200px; overflow: hidden; }
  body {
    background: var(--bg);
    font-family: "Arimo", Arial, sans-serif;
    display: flex;
    flex-direction: column;
    align-items: center;
    justify-content: center;
    gap: 60px;
  }
  .card {
    width: 840px;
    height: 480px;
    border-radius: 36px;
    box-shadow: 0 10px 30px rgba(0,0,0,0.18);
    position: relative;
  }

  /* Back side: brand + url */
  .card-back {
    background: var(--card-light);
    display: flex;
    flex-direction: column;
    align-items: center;
    justify-content: center;
    gap: 34px;
  }
  .brand {
    display: flex;
    align-items: center;
    gap: 22px;
  }
  .brand-dot {
    width: 58px; height: 58px;
    border-radius: 50%;
    background: var(--brand-blue);
  }
  .brand-name {
    color: var(--brand-blue);
    font-weight: 700;
    font-size: 74px;
    letter-spacing: -1px;
  }
  .site-url {
    color: var(--brand-blue);
    font-size: 34px;
    letter-spacing: 7px;
  }

  /* Front side: person + contact */
  .card-front {
    background: radial-gradient(circle at 62% 40%, var(--card-dark-glow) 0%, var(--card-dark) 60%);
    color: var(--ink-light);
    display: flex;
    align-items: center;
    padding: 0 60px 0 110px;
  }
  .person {
    text-align: right;
    width: 300px;
  }
  .person-name {
    font-weight: 700;
    font-size: 40px;
    letter-spacing: 0.5px;
  }
  .person-role {
    font-size: 22px;
    margin-top: 4px;
  }
  .contact {
    margin-left: 40px;
    display: flex;
    flex-direction: column;
    gap: 34px;
  }
  .contact-group {
    border-left: 1.5px solid var(--rule);
    padding-left: 34px;
    display: flex;
    flex-direction: column;
    gap: 8px;
  }
  .contact-row {
    display: flex;
    align-items: flex-start;
    gap: 12px;
    font-size: 21px;
    line-height: 1.25;
  }
  .contact-icon {
    flex: none;
    width: 22px; height: 22px;
    margin-top: 2px;
  }
</style>
</head>
<body>

  <section class="card card-back" aria-label="Card back">
    <div class="brand">
      <span class="brand-dot"></span>
      <span class="brand-name">Brightpath Media</span>
    </div>
    <div class="site-url">www.brightpathmedia.com</div>
  </section>

  <section class="card card-front" aria-label="Card front">
    <div class="person">
      <div class="person-name">JOHN DOE</div>
      <div class="person-role">Director</div>
    </div>
    <div class="contact">
      <div class="contact-group">
        <div class="contact-row">
          <svg class="contact-icon" viewBox="0 0 24 24" aria-hidden="true">
            <circle cx="12" cy="12" r="11" fill="#fff"/>
            <path d="M12 5a4.5 4.5 0 0 0-4.5 4.5C7.5 13 12 18 12 18s4.5-5 4.5-8.5A4.5 4.5 0 0 0 12 5z" fill="#2e3033"/>
            <circle cx="12" cy="9.5" r="1.7" fill="#fff"/>
          </svg>
          <span>Dummy city<br>Dummy Country Land</span>
        </div>
      </div>
      <div class="contact-group">
        <div class="contact-row">
          <svg class="contact-icon" viewBox="0 0 24 24" aria-hidden="true">
            <circle cx="12" cy="12" r="11" fill="#fff"/>
            <path d="M6 10c0-2 2.5-3 6-3s6 1 6 3l-2 1-1-2h-6l-1 2zM8 12h8l1 5H7z" fill="#2e3033"/>
          </svg>
          <span>1-234-567890</span>
        </div>
        <div class="contact-row">
          <svg class="contact-icon" viewBox="0 0 24 24" aria-hidden="true">
            <circle cx="12" cy="12" r="11" fill="#fff"/>
            <rect x="8" y="6" width="8" height="5" fill="#2e3033"/>
            <rect x="6" y="11" width="12" height="7" rx="1" fill="#2e3033"/>
          </svg>
          <span>1-234-567890</span>
        </div>
        <div class="contact-row">
          <svg class="contact-icon" viewBox="0 0 24 24" aria-hidden="true">
            <circle cx="12" cy="12" r="11" fill="#fff"/>
            <rect x="6.5" y="8" width="11" height="8" rx="1" fill="#2e3033"/>
            <path d="M7 8.5l5 4 5-4" stroke="#fff" stroke-width="1.2" fill="none"/>
          </svg>
          <span>john@brightpathmedia.com</span>
        </div>
      </div>
    </div>
  </section>

</body>
</html>
```